Kenwick Falcons FC Website

We are looking to develop a new website for Kenwick FC. Kenwick FC has now joined with Kenwick Falcons FC and we are looking at a website that can work for both clubs. Kenwick FC play in a local park football competition while kenwick Falcons are a Semi Professional team that plays in the Coastal Premier Division Competition. What we are after is two separate website off the one platform. I have attached both team logos for you to visualise. Also you can look at the existing kenwick website www.kenwickfc-demo.com.au. We are looking for a huge improvement in the website and it will be imperative we have links to sponsors and the sponsors can get regular visuals. Weare looking to move this club forward and have a very professional website that can communicate clearly with the community.

Hi All,

Please remember that the website is to represent two clubs;
1. Kenwick Falcons FC (Competes in Semi Professional League)
2. Kenwick FC (Compete in HBJCA League which is a lower level)

Further to this the Kenwick Falcons FC page will require a player profile page which will show photos of each player and a little bio on each.

Thanks

Reason: Would like to spend more time review existing and new designs

```html
<!DOCTYPE html>
<html lang="en">
<head>
<meta charset="utf-8">
<title>Kenwick FC / Kenwick Falcons FC — Official Website</title>
<link rel="stylesheet" href="https://fonts.googleapis.com/css2?family=Crimson+Text:wght@400;600;700&family=Arimo:wght@400&display=swap">
<style>
  :root {
    --page-bg: #f2f1ef;
    --footer-bg: #ffffff;
    --ink: #2e2e2e;
    --title-ink: #3a3a3a;
    --body-ink: #4a4a4a;
    --muted: #7a7a7a;
    --brand-red: #d00000;
    --link-red: #e05555;
    --panel-dark: rgba(40, 40, 40, 0.9);
    --rule: #d9d8d5;
    --white: #ffffff;
  }
  * { margin: 0; padding: 0; box-sizing: border-box; }
  html, body { width: 1200px; height: 1003px; overflow: hidden; }
  body {
    background: var(--page-bg);
    font-family: "Crimson Text", Georgia, serif;
    color: var(--ink);
    position: relative;
  }
  a { text-decoration: none; }

  .hero {
    position: absolute; left: 0; top: 0; width: 1200px; height: 439px;
    background:
      radial-gradient(ellipse 420px 240px at 640px 170px, rgba(190,170,120,0.55), transparent 70%),
      radial-gradient(ellipse 380px 260px at 1000px 260px, rgba(40,120,70,0.45), transparent 70%),
      linear-gradient(180deg, #b9b39b 0%, #a9a486 40%, #7f8a52 70%, #5f6e35 100%);
  }
  .hero-tagline {
    position: absolute; left: 474px; top: 132px; width: 253px; height: 36px;
    background: var(--panel-dark); color: var(--white);
    font-size: 23px; line-height: 36px; text-align: center; white-space: nowrap;
  }
  .hero-tagline strong { font-weight: 600; }
  .hero-arrow {
    position: absolute; top: 198px; width: 43px; height: 43px;
    background: var(--panel-dark);
  }
  .hero-arrow--prev { left: 48px; }
  .hero-arrow--next { left: 1101px; }
  .hero-arrow svg { display: block; }

  .club-card {
    position: absolute; top: 310px; width: 264px; height: 257px;
    background: var(--white); border-top: 9px solid var(--brand-red);
    text-align: center;
  }
  .club-card::after {
    content: ""; position: absolute; left: 12px; right: 12px; bottom: -14px; height: 14px;
    background: radial-gradient(ellipse at top, rgba(0,0,0,0.28), transparent 70%);
  }
  .club-card--local { left: 293px; }
  .club-card--senior { left: 643px; }
  .club-crest {
    position: absolute; left: 0; right: 0; top: 30px;
    display: flex; flex-direction: column; align-items: center; gap: 10px;
  }
  .club-crest-mark {
    width: 84px; height: 84px; border-radius: 50%; background: var(--brand-red);
  }
  .club-crest-name {
    font-size: 15px; font-weight: 700; color: var(--brand-red);
    text-transform: uppercase; letter-spacing: 1.5px; line-height: 20px;
  }
  .club-title {
    position: absolute; left: 0; right: 0; top: 189px;
    font-size: 22px; line-height: 28px; font-weight: 700; color: var(--title-ink);
  }

  .welcome {
    position: absolute; left: 160px; top: 610px; width: 880px; text-align: center;
  }
  .welcome-heading { font-size: 24px; font-weight: 600; color: var(--ink); line-height: 36px; }
  .welcome-rule { display: block; margin-top: 6px; }
  .welcome-motto {
    margin-top: 14px; font-size: 19px; font-weight: 400; color: var(--brand-red); line-height: 26px;
  }
  .welcome-intro {
    margin-top: 11px; font-size: 13.4px; line-height: 17.6px; color: var(--body-ink);
  }
  .register-button {
    position: absolute; left: 528px; top: 802px; width: 144px; height: 32px;
    background: var(--brand-red); padding: 3px;
  }
  .register-button span {
    display: block; height: 100%; border: 1px solid rgba(255,255,255,0.7);
    color: var(--white); font-family: "Arimo", Arial, sans-serif; font-size: 13px;
    line-height: 24px; text-align: center;
  }

  .site-footer {
    position: absolute; left: 0; top: 874px; width: 1200px; height: 129px;
    background: var(--footer-bg); border-top: 1px solid var(--rule);
    font-family: "Arimo", Arial, sans-serif; text-align: center;
  }
  .copyright { margin-top: 27px; font-size: 12px; color: var(--muted); line-height: 16px; }
  .copyright b { font-weight: 400; color: #333; }
  .privacy-link {
    font-size: 12px; color: var(--link-red); line-height: 16px; display: inline-block;
    text-decoration: underline;
  }
  .social-links { margin-top: 24px; display: flex; justify-content: center; gap: 12px; }
  .social-links a { font-size: 11px; color: var(--brand-red); }
</style>
</head>
<body>

  <header class="hero" role="img" aria-label="Action photo of a striker kicking a football as a diving goalkeeper reaches for it on a grass pitch">
    <div class="hero-tagline">The <strong>Game</strong> Is About <strong>Glory</strong></div>
    <a class="hero-arrow hero-arrow--prev" href="#" aria-label="Previous slide">
      <svg width="43" height="43" viewBox="0 0 43 43"><polyline points="26,10 15,21.5 26,33" fill="none" stroke="#fff" stroke-width="2.5"/></svg>
    </a>
    <a class="hero-arrow hero-arrow--next" href="#" aria-label="Next slide">
      <svg width="43" height="43" viewBox="0 0 43 43"><polyline points="17,10 28,21.5 17,33" fill="none" stroke="#fff" stroke-width="2.5"/></svg>
    </a>
  </header>

  <a class="club-card club-card--local" href="#">
    <div class="club-crest">
      <div class="club-crest-mark"></div>
      <div class="club-crest-name">Kenwick FC</div>
    </div>
    <div class="club-title">Kenwick FC</div>
  </a>

  <a class="club-card club-card--senior" href="#">
    <div class="club-crest">
      <div class="club-crest-mark"></div>
      <div class="club-crest-name">Kenwick Falcons FC</div>
    </div>
    <div class="club-title">Kenwick Falcons FC</div>
  </a>

  <section class="welcome">
    <h1 class="welcome-heading">Welcome to Our Official Website</h1>
    <svg class="welcome-rule" width="880" height="10" viewBox="0 0 880 10">
      <polyline points="0,1 431,1 440,9 449,1 880,1" fill="none" stroke="#d9d8d5" stroke-width="1.5"/>
    </svg>
    <h2 class="welcome-motto">Play the game you love and love the game you play!</h2>
    <p class="welcome-intro">"Lorem ipsum dolor sit amet, consectetur adipisicing elit, sed do eiusmod tempor incididunt ut labore et dolore magna aliqua. Ut enim ad minim veniam, quis nostrud<br>exercitation ullamco laboris nisi ut aliquip ex ea commodo consequat. Duis aute irure dolor in reprehenderit in voluptate<br>velit esse cillum dolore eu fugiat nulla pariatur. Excepteur sint occaecat cupidatat non proident,<br>sunt in culpa qui officia deserunt mollit anim id est laborum."</p>
  </section>

  <a class="register-button" href="#"><span>REGISTER ONLINE</span></a>

  <footer class="site-footer">
    <p class="copyright">Copyright © <b>Kenwick FC / Kenwick Falcons FC</b> 2014. All Rights Reserved.</p>
    <a class="privacy-link" href="#">Privacy Policy</a>
    <nav class="social-links">
      <a href="#">Friendly</a>
      <a href="#">Chirper</a>
      <a href="#">Linkwork</a>
    </nav>
  </footer>

</body>
</html>
```